Web design for Modeling agency

We are looking for re-designing our modeling agency website.
Current website: lunafaces.com our competitor: KTRfaces.com
http://brisaface.fr/
https://www.corvelmanagement.com/models/
https://www.hedwig-faces.de
https://www.rustmanagement.co.uk
https://www.quorbfaces.com
https://www.harborlightfaces.com

Target Market(s)

modeling agency

Industry/Entity Type

modeling agency

Number of Pages Required

5+ page

Font styles to use
Other font styles liked:
• base on logo guidline

Requirements
Nice to have
• current website: lunafaces.com our competitor: KTRfaces.com

```html
<!DOCTYPE html>
<html lang="en">
<head>
<meta charset="utf-8">
<title>Luna Models</title>
<link rel="stylesheet" href="https://fonts.googleapis.com/css2?family=Montserrat:wght@300;400;500;600;700&display=swap">
<style>
:root{
  --accent:#a98468;
  --accent-dark:#6b4e3f;
  --ink:#1e1e1e;
  --muted:#6f6f6f;
  --peach:#fcefe6;
  --paper:#fbfbfb;
  --footer:#2d1714;
  --white:#ffffff;
}
*{box-sizing:border-box;margin:0;padding:0}
html,body{width:1200px;height:3492px;overflow:hidden;background:var(--white)}
body{position:relative;font-family:'Montserrat',sans-serif;color:var(--ink)}
a{color:inherit;text-decoration:none}

/* header */
.site-header{position:absolute;left:0;top:0;width:1200px;height:81px;background:var(--white);z-index:3}
.burger{position:absolute;left:72px;top:30px;width:24px}
.burger span{display:block;height:1px;background:var(--accent);margin-bottom:6px}
.nav-link{position:absolute;top:30px;font-size:13px;letter-spacing:.5px;color:#555;transform:translateX(-50%)}
.nav-link.active{font-weight:700;color:var(--ink)}
.nav-link.active::after{content:"";display:block;height:1px;background:var(--accent);margin-top:8px;width:34px;margin-left:auto;margin-right:auto}
.login{position:absolute;left:1009px;top:22px;width:93px;height:33px;border:1.5px solid var(--accent-dark);font-size:13px;color:#555;display:flex;align-items:center;justify-content:center}
.logo-tab{position:absolute;left:470px;top:0;z-index:4}
.brand{position:absolute;left:579px;transform:translateX(-50%);text-align:center;color:var(--accent);font-weight:300;z-index:5;white-space:nowrap}
.brand-name{top:6px;font-size:54px;letter-spacing:-1px;line-height:60px}
.brand-sub{top:73px;font-size:19px;letter-spacing:1px}

/* hero */
.hero{position:absolute;left:0;top:81px;width:1200px;height:647px;background:
  radial-gradient(ellipse 260px 420px at 390px 420px,#3fae6e 0%,rgba(63,174,110,0) 100%),
  radial-gradient(ellipse 280px 440px at 740px 430px,#e6388f 0%,rgba(230,56,143,0) 100%),
  linear-gradient(180deg,#c9c2bd 0%,#8b7f7a 45%,#4c4442 100%)}
.hero-shade{position:absolute;inset:0;background:rgba(0,0,0,.1)}
.hero-kicker{position:absolute;left:0;width:1200px;top:282px;text-align:center;color:var(--white);font-size:36px;font-weight:300;letter-spacing:9px}
.hero-title{position:absolute;left:0;width:1200px;top:318px;text-align:center;color:transparent;-webkit-text-stroke:1.5px var(--white);font-size:72px;font-weight:500;letter-spacing:4px;line-height:1}
.rail-icon{position:absolute;left:1149px;width:26px;height:26px;display:flex;align-items:center;justify-content:center;color:var(--white);font-size:10px;font-weight:600}
.rail-icon.boxed{border:1px solid var(--white)}
.scroll-line{position:absolute;left:1162px;top:403px;width:1px;height:66px;background:var(--white)}
.scroll-label{position:absolute;left:1162px;top:530px;transform:translate(-50%,-50%) rotate(-90deg);color:var(--white);font-size:10px;letter-spacing:1.5px;white-space:nowrap}

/* section titles */
.section-title{position:absolute;left:0;width:1200px;text-align:center;font-size:31px;font-weight:300;letter-spacing:4px;color:var(--ink)}
.section-title b{font-weight:700}
.rule{position:absolute;left:570px;width:58px;height:3px;background:var(--accent)}

/* featured */
.featured{position:absolute;left:0;top:728px;width:1200px;height:560px;background:var(--peach)}
.model-photo{position:absolute;width:240px;height:240px;border-radius:50%}
.model-name{position:absolute;width:260px;text-align:center;font-size:20px;font-weight:400;transform:translateX(-50%)}
.model-link{position:absolute;width:200px;text-align:center;font-size:14px;color:#444;text-decoration:underline;transform:translateX(-50%)}

/* news slider */
.news-card{position:absolute;top:1447px;height:434px}
.news-caption{position:absolute;left:0;right:0;bottom:0;height:83px;background:rgba(50,34,28,.72);color:var(--white);text-align:center;font-size:15px;font-weight:600;padding-top:22px;letter-spacing:.3px}
.news-caption small{display:block;font-size:13px;margin-top:6px}
.arrow{position:absolute;top:1640px}

/* videos */
.video{position:absolute;top:2050px;height:408px}
.video.dim{opacity:.55}
.play{position:absolute;left:576px;top:2184px}
.play-label{position:absolute;left:297px;width:617px;top:2274px;text-align:center;color:var(--white);font-size:22px;font-weight:300;letter-spacing:5px}

/* popular */
.popular-bg{position:absolute;left:0;top:2460px;width:1200px;height:785px;background:var(--paper)}
.pop-card{position:absolute;top:2620px;width:246px;height:298px;background:var(--white);box-shadow:0 2px 12px rgba(0,0,0,.05)}
.pop-card.active{height:305px;background:var(--accent-dark);color:var(--white)}
.pop-photo{width:246px;height:190px}
.pop-title{position:absolute;left:34px;top:222px;font-size:13px;font-weight:700;color:var(--accent-dark)}
.pop-text{position:absolute;left:34px;top:246px;font-size:11px;line-height:18px;color:#777}
.pop-card.active .pop-title{left:28px;top:214px;color:var(--white)}
.pop-card.active .pop-text{left:28px;top:240px;color:var(--white)}

/* follow */
.insta{position:absolute;top:3058px;height:183px}
.insta-mark{position:absolute;left:476px;top:3137px;width:26px;height:26px;border-radius:50%;border:2px solid var(--white)}

/* footer */
.site-footer{position:absolute;left:0;top:3245px;width:1200px;height:247px;background:var(--footer);color:var(--white)}
.foot-brand{position:absolute;left:0;width:1200px;text-align:center;font-weight:300}
.foot-link{position:absolute;top:120px;font-size:12px;transform:translateX(-50%);letter-spacing:.3px}
.copyright{position:absolute;left:0;width:1200px;top:157px;text-align:center;font-size:11px;color:#d9c9c2}
.foot-social{position:absolute;top:186px;width:30px;height:30px;border-radius:50%;background:var(--white);color:var(--footer);font-size:13px;font-weight:700;display:flex;align-items:center;justify-content:center}
</style>
</head>
<body>

<header class="site-header">
  <div class="burger"><span></span><span></span><span></span></div>
  <a class="nav-link active" style="left:187px">MEN</a>
  <a class="nav-link" style="left:281px">WOMEN</a>
  <a class="nav-link" style="left:386px">TALENT</a>
  <a class="nav-link" style="left:755px">VIDEO</a>
  <a class="nav-link" style="left:853px">ABOUT</a>
  <a class="nav-link" style="left:949px">NEWS</a>
  <a class="login">LOGIN</a>
</header>
<svg class="logo-tab" width="208" height="108" viewBox="0 0 208 108"><polygon points="0,81 208,81 182,106 26,106" fill="#ffffff"/></svg>
<div class="brand brand-name">LUNA</div>
<div class="brand brand-sub">MODELS</div>

<section class="hero">
  <div class="hero-shade" role="img" aria-label="Two models in bright green and pink coats posing on a city street"></div>
  <div class="hero-kicker">WELCOME TO</div>
  <div class="hero-title">LUNA MODELS</div>
</section>
<div class="rail-icon boxed" style="top:256px" aria-label="Pictly">P</div>
<div class="rail-icon" style="top:297px" aria-label="Snapora">S</div>
<div class="rail-icon" style="top:336px" aria-label="Chirpa">C</div>
<div class="scroll-line"></div>
<div class="scroll-label">&lsaquo; SCROLL DOWN</div>

<section class="featured">
  <h2 class="section-title" style="top:72px">FEATURED <b>MODELS</b></h2>
  <div class="rule" style="top:120px"></div>
</section>
<div class="model-photo" style="left:86px;top:898px;background:radial-gradient(circle at 50% 40%,#c59a82,#6b4a3c 70%,#e4e4e4 71%)" role="img" aria-label="Portrait of a male model"></div>
<div class="model-photo" style="left:350px;top:896px;background:radial-gradient(circle at 50% 45%,#e4d6c8,#a8917d)" role="img" aria-label="Female model seated in a woven chair"></div>
<div class="model-photo" style="left:635px;top:898px;background:radial-gradient(circle at 50% 45%,#9a6a50,#2a1c18 75%)" role="img" aria-label="Portrait of a female model with natural curls"></div>
<div class="model-photo" style="left:900px;top:896px;background:linear-gradient(90deg,#6a9fbf 0%,#b48676 55%,#6a9fbf 100%)" role="img" aria-label="Female model in profile against a blue sky"></div>
<div class="model-name" style="left:203px;top:1157px">LUNA MODEL NAME</div>
<div class="model-link" style="left:203px;top:1184px">VIEW DETAILS</div>
<div class="model-name" style="left:466px;top:1154px">LUNA MODEL NAME</div>
<div class="model-link" style="left:466px;top:1181px">VIEW DETAILS</div>
<div class="model-name" style="left:752px;top:1157px">LUNA MODEL NAME</div>
<div class="model-link" style="left:752px;top:1184px">VIEW DETAILS</div>
<div class="model-name" style="left:1015px;top:1154px">LUNA MODEL NAME</div>
<div class="model-link" style="left:1015px;top:1181px">VIEW DETAILS</div>

<h2 class="section-title" style="top:1364px">LATEST <b>NEWS</b></h2>
<div class="rule" style="top:1410px"></div>
<article class="news-card" style="left:0;width:399px;background:linear-gradient(160deg,#a9b6c2 0%,#7c8ea0 35%,#2a3fd0 60%,#1f2540 100%)" role="img" aria-label="Model in a blue tulle gown leaning on a car">
  <div class="news-caption">DALIA VERNE &nbsp;|&nbsp; FW 2021<small>VIEW MORE</small></div>
</article>
<article class="news-card" style="left:400px;width:397px;background:linear-gradient(180deg,#eadccd 0%,#e2c7ae 35%,#d88fb0 60%,#c9c46a 100%)" role="img" aria-label="Model in a printed pink and green blouse">
  <div class="news-caption" style="background:rgba(60,38,30,.85)">DALIA VERNE &nbsp;|&nbsp; FW 2021<small>VIEW MORE</small></div>
</article>
<article class="news-card" style="left:799px;width:401px;background:linear-gradient(135deg,#2e2e2e,#8a8a8a 50%,#dcdcdc)" role="img" aria-label="Black and white close-up portrait of a male model">
  <div class="news-caption">DALIA VERNE &nbsp;|&nbsp; FW 2021<small>VIEW MORE</small></div>
</article>
<svg class="arrow" style="left:30px" width="26" height="52" viewBox="0 0 26 52"><polyline points="24,2 2,26 24,50" fill="none" stroke="#fff" stroke-width="2"/></svg>
<svg class="arrow" style="left:1142px" width="26" height="52" viewBox="0 0 26 52"><polyline points="2,2 24,26 2,50" fill="none" stroke="#fff" stroke-width="2"/></svg>

<h2 class="section-title" style="top:1948px">LATEST <b>VIDEOS</b></h2>
<div class="rule" style="top:1994px"></div>
<div class="video dim" style="left:0;width:286px;background:linear-gradient(120deg,#3b3a40,#e0a24e 50%,#d8c48a)" role="img" aria-label="Video still of a model by a yellow building"></div>
<div class="video" style="left:297px;width:617px;background:linear-gradient(110deg,#23306e,#34408c 40%,#d9a233 70%,#e07a2a)" role="img" aria-label="Video still of a model in a yellow suit beside a blue car"></div>
<div class="video dim" style="left:925px;width:275px;background:linear-gradient(120deg,#2b3a8a,#5a6aa8 60%,#aeb6d2)" role="img" aria-label="Video still of a blue car"></div>
<svg class="play" width="78" height="78" viewBox="0 0 78 78"><circle cx="39" cy="39" r="36" fill="none" stroke="#fff" stroke-width="4"/><polygon points="30,22 58,39 30,56" fill="#fff"/></svg>
<div class="play-label">PLAY NOW</div>

<div class="popular-bg"></div>
<h2 class="section-title" style="top:2522px">POPULAR <b>NEWS</b></h2>
<div class="rule" style="top:2567px"></div>
<article class="pop-card active" style="left:70px">
  <div class="pop-photo" style="background:linear-gradient(160deg,#b08a66,#e8cdb6)" role="img" aria-label="Close-up portrait of a blonde model"></div>
  <div class="pop-title">LOREM IPSUM DOLOR SIT</div>
  <div class="pop-text">Lorem ipsum dolor sit amet,<br>consectetur adipiscing</div>
</article>
<article class="pop-card" style="left:335px">
  <div class="pop-photo" style="background:linear-gradient(180deg,#2f8f9b,#e0b08e 60%,#f0ece6)" role="img" aria-label="Model wearing a teal head wrap"></div>
  <div class="pop-title">LOREM IPSUM DOLOR SIT</div>
  <div class="pop-text">Lorem ipsum dolor sit amet,<br>consectetur adipiscing</div>
</article>
<article class="pop-card" style="left:598px">
  <div class="pop-photo" style="background:linear-gradient(180deg,#6f8aa8,#3a2e2c 70%)" role="img" aria-label="Model with windswept dark hair"></div>
  <div class="pop-title">LOREM IPSUM DOLOR SIT</div>
  <div class="pop-text">Lorem ipsum dolor sit amet,<br>consectetur adipiscing</div>
</article>
<article class="pop-card" style="left:864px">
  <div class="pop-photo" style="background:linear-gradient(180deg,#f3efec,#b07a5e 55%,#7a4a36)" role="img" aria-label="Male model with curly hair"></div>
  <div class="pop-title">LOREM IPSUM DOLOR SIT</div>
  <div class="pop-text">Lorem ipsum dolor sit amet,<br>consectetur adipiscing</div>
</article>

<h2 class="section-title" style="top:2996px;font-size:24px">FOLLOW <b>US</b></h2>
<div class="insta" style="left:0;width:160px;background:linear-gradient(160deg,#7a5a48,#e9dcc9)" role="img" aria-label="Model in a cream blouse"></div>
<div class="insta" style="left:165px;width:211px;background:linear-gradient(160deg,#4a78a8,#3b3230)" role="img" aria-label="Model in a plaid blazer"></div>
<div class="insta" style="left:382px;width:211px;background:linear-gradient(180deg,#d9d5d8,#9aa8d2)" role="img" aria-label="Model in a lilac tulle dress"></div>
<div class="insta-mark"></div>
<div class="insta" style="left:598px;width:210px;background:linear-gradient(160deg,#3a2a1e,#c89a5c)" role="img" aria-label="Model wearing large glasses"></div>
<div class="insta" style="left:812px;width:209px;background:linear-gradient(160deg,#c8a98e,#b23a2a 60%,#5a4a42)" role="img" aria-label="Model in a red coat"></div>
<div class="insta" style="left:1026px;width:174px;background:linear-gradient(160deg,#2b2e34,#c4603a)" role="img" aria-label="Model in an orange top"></div>

<footer class="site-footer">
  <div class="foot-brand" style="top:14px;font-size:44px;letter-spacing:-1px">LUNA</div>
  <div class="foot-brand" style="top:75px;font-size:15px;letter-spacing:.5px">MODEL MGMT</div>
  <a class="foot-link" style="left:240px">MEN</a>
  <a class="foot-link" style="left:347px">WOMEN</a>
  <a class="foot-link" style="left:465px">TALENT</a>
  <a class="foot-link" style="left:578px">VIDEO</a>
  <a class="foot-link" style="left:688px">ABOUT</a>
  <a class="foot-link" style="left:797px">NEWS</a>
  <a class="foot-link" style="left:925px">CONTACT US</a>
  <div class="copyright">copyright © 2021 luna | All Rights Reserved</div>
  <a class="foot-social" style="left:533px" aria-label="Pictly">P</a>
  <a class="foot-social" style="left:568px" aria-label="Chirpa">C</a>
  <a class="foot-social" style="left:603px" aria-label="Vidora">V</a>
  <a class="foot-social" style="left:640px" aria-label="Snapora">S</a>
</footer>

</body>
</html>
```